Penwhistle & Partners - stylish and sophisticated box design required!

We need a packaging design for our online training company based in Australia called 'Penwhistle & Partners'. We will be sending out Slate Lite`s as well as an A4 ring bound document of 60 pages. We would like the Slate to sit at the bottom of the box with the A4 document sitting on top. Inside the box, there will be fine paper covering the product. Maybe we could have a pattern or the logo on this.

The design should be a cardboard pull out box, black in colour with the logo embossed on the cover (attached institute logo). We are looking for the packaging to communicate sophistication and style.
An examples of a cardboard box shape we quite like could be found on this site:

http://tasks.brieflane-example.com.au/task.aspx?id=71305

I have uploaded two different logos as the previous logo was not nice!

Industry/Entity Type

It Company

```html
<!DOCTYPE html>
<html lang="en">
<head>
<meta charset="utf-8">
<title>Penwhistle &amp; Partners – Pull-out Box Dieline</title>
<link href="https://fonts.googleapis.com/css2?family=Cinzel:wght@400&display=swap" rel="stylesheet">
<style>
  :root {
    --paper: #ffffff;
    --board: #231f20;
    --fold: #4a4647;
    --emboss: #8a8788;
    --band-light: #bdbdbd;
    --band-dark: #4a4748;
  }
  html, body {
    margin: 0;
    padding: 0;
    width: 1200px;
    height: 1000px;
    overflow: hidden;
    background: var(--paper);
  }
  .canvas {
    position: relative;
    width: 1200px;
    height: 1000px;
  }
  .panel {
    position: absolute;
    background: var(--board);
  }
  .body-wrap { left: 190px; top: 239px; width: 816px; height: 568px; }
  .flap-top { left: 624px; top: 184px; width: 382px; height: 55px; }
  .flap-bottom { left: 624px; top: 807px; width: 382px; height: 54px; }
  .fold-line {
    position: absolute;
    background: var(--fold);
  }
  .fold-spine-left { left: 572px; top: 239px; width: 1px; height: 568px; }
  .fold-spine-right { left: 624px; top: 239px; width: 1px; height: 568px; }
  .fold-flap-top { left: 624px; top: 238px; width: 382px; height: 1px; }
  .fold-flap-bottom { left: 624px; top: 807px; width: 382px; height: 1px; }
  .band {
    position: absolute;
    left: 190px;
    width: 816px;
    background: linear-gradient(to bottom, var(--band-dark), var(--band-light));
  }
  .band-upper { top: 430px; height: 12px; }
  .band-lower { top: 669px; height: 18px; }
  .score-gap {
    position: absolute;
    left: 190px;
    top: 700px;
    width: 816px;
    height: 6px;
    background: var(--paper);
  }
  .emblem {
    position: absolute;
    display: flex;
    align-items: center;
    justify-content: center;
    border-radius: 50%;
    border: 2px solid var(--emboss);
    box-sizing: border-box;
  }
  .emblem-name {
    font-family: "Cinzel", serif;
    color: var(--emboss);
    text-align: center;
    letter-spacing: 0.06em;
    line-height: 1.3;
    white-space: nowrap;
  }
  .emblem-back { left: 319px; top: 492px; width: 128px; height: 128px; }
  .emblem-back .emblem-name { font-size: 12px; }
  .emblem-front { left: 732px; top: 472px; width: 168px; height: 168px; }
  .emblem-front .emblem-name { font-size: 16px; }
</style>
</head>
<body>
  <main class="canvas">
    <div class="panel flap-top"></div>
    <div class="panel body-wrap"></div>
    <div class="panel flap-bottom"></div>

    <div class="fold-line fold-spine-left"></div>
    <div class="fold-line fold-spine-right"></div>
    <div class="fold-line fold-flap-top"></div>
    <div class="fold-line fold-flap-bottom"></div>

    <div class="band band-upper"></div>
    <div class="band band-lower"></div>
    <div class="score-gap"></div>

    <div class="emblem emblem-back">
      <span class="emblem-name">Penwhistle<br>&amp; Partners</span>
    </div>
    <div class="emblem emblem-front">
      <span class="emblem-name">Penwhistle<br>&amp; Partners</span>
    </div>
  </main>
</body>
</html>
```